Kestrel Signs Facebook Banner Design

Design a facebook banner for a sign company. I would like to have a modern approach to it.

Product Offering:
Signs
Banners
Decals
Commercial Wraps

```html
<!DOCTYPE html>
<html lang="en">
<head>
<meta charset="utf-8">
<title>Kestrel Signs – Facebook Banner</title>
<link rel="stylesheet" href="https://fonts.googleapis.com/css2?family=Poppins:wght@800&family=Questrial&display=swap">
<style>
  :root {
    --page-bg: #b9b9b9;
    --card-bg: #ffffff;
    --brand-red: #e21f2e;
    --deep-red: #b80f1c;
    --charcoal: #1f1f1f;
    --ink: #2b2b2b;
    --white: #ffffff;
  }
  * { margin: 0; padding: 0; box-sizing: border-box; }
  html, body { width: 900px; height: 1200px; overflow: hidden; }
  body { background: var(--page-bg); position: relative; }

  .banner {
    position: absolute;
    left: 62px; top: 430px;
    width: 778px; height: 341px;
    background: var(--card-bg);
    overflow: hidden;
  }
  .banner-art { position: absolute; inset: 0; width: 778px; height: 341px; }

  .brand-name {
    position: absolute;
    left: 0; width: 778px; top: 42px;
    text-align: center;
    font-family: "Poppins", sans-serif;
    font-weight: 800;
    font-size: 25px;
    line-height: 24px;
    color: var(--ink);
    text-transform: uppercase;
  }

  .headline {
    position: absolute;
    left: 88px; top: 86px;
    font-family: "Poppins", sans-serif;
    font-weight: 800;
    color: var(--white);
    text-transform: uppercase;
  }
  .headline-top { display: block; font-size: 58px; line-height: 56px; letter-spacing: 1px; }
  .headline-line { display: block; font-size: 31px; line-height: 35px; }

  .service-list {
    position: absolute;
    left: 509px; top: 82px;
    list-style: none;
    font-family: "Questrial", sans-serif;
    color: var(--white);
    font-size: 23px;
  }
  .service-item { display: flex; align-items: flex-start; margin-bottom: 9px; line-height: 24px; }
  .service-item .tick { flex: none; width: 23px; height: 23px; margin-right: 7px; }

  .phone {
    position: absolute;
    left: 529px; top: 272px;
    display: flex; align-items: center;
    font-family: "Questrial", sans-serif;
    font-size: 20px;
    color: var(--ink);
    letter-spacing: 0.5px;
  }
  .phone-icon { width: 19px; height: 19px; margin-right: 4px; }
</style>
</head>
<body>
  <section class="banner">
    <svg class="banner-art" viewBox="0 0 1296 569" aria-hidden="false">
      <defs>
        <linearGradient id="bandFill" gradientUnits="userSpaceOnUse" x1="95" y1="0" x2="1201" y2="0">
          <stop offset="0" stop-color="#d41626"/>
          <stop offset="0.38" stop-color="var(--deep-red)"/>
          <stop offset="0.6" stop-color="#2a2a2a"/>
          <stop offset="1" stop-color="var(--charcoal)"/>
        </linearGradient>
        <linearGradient id="personFill" x1="0" y1="0" x2="0" y2="1">
          <stop offset="0" stop-color="#d92030"/>
          <stop offset="0.5" stop-color="#c41a28"/>
          <stop offset="1" stop-color="#2e2e2e"/>
        </linearGradient>
      </defs>
      <path class="band" fill="url(#bandFill)"
        d="M130,68 L407,68 Q647,252 887,68 L1166,68 A35,35 0 0 1 1201,103 L1201,409 A35,35 0 0 1 1166,444 L700,444 L700,501 L130,501 A35,35 0 0 1 95,466 L95,103 A35,35 0 0 1 130,68 Z"/>
      <g role="img" aria-label="Photo of a smiling sign technician in a red cap, red shirt and dark overalls giving a peace sign">
        <path fill="url(#personFill)" d="M530,569 L545,250 Q560,147 690,147 Q830,150 845,300 L850,569 Z"/>
      </g>
    </svg>

    <div class="brand-name">Kestrel<br>Signs</div>

    <h1 class="headline">
      <span class="headline-top">Top</span>
      <span class="headline-line">Sign Design</span>
      <span class="headline-line">&amp; Printing</span>
      <span class="headline-line">Experts</span>
    </h1>

    <ul class="service-list">
      <li class="service-item">
        <svg class="tick" viewBox="0 0 24 24"><rect width="24" height="24" rx="4" fill="var(--brand-red)"/><path d="M6 12.5l4 4 8-9" fill="none" stroke="var(--white)" stroke-width="3" stroke-linecap="round" stroke-linejoin="round"/></svg>
        <span>SIGNS</span>
      </li>
      <li class="service-item">
        <svg class="tick" viewBox="0 0 24 24"><rect width="24" height="24" rx="4" fill="var(--brand-red)"/><path d="M6 12.5l4 4 8-9" fill="none" stroke="var(--white)" stroke-width="3" stroke-linecap="round" stroke-linejoin="round"/></svg>
        <span>BANNERS</span>
      </li>
      <li class="service-item">
        <svg class="tick" viewBox="0 0 24 24"><rect width="24" height="24" rx="4" fill="var(--brand-red)"/><path d="M6 12.5l4 4 8-9" fill="none" stroke="var(--white)" stroke-width="3" stroke-linecap="round" stroke-linejoin="round"/></svg>
        <span>DECALS</span>
      </li>
      <li class="service-item">
        <svg class="tick" viewBox="0 0 24 24"><rect width="24" height="24" rx="4" fill="var(--brand-red)"/><path d="M6 12.5l4 4 8-9" fill="none" stroke="var(--white)" stroke-width="3" stroke-linecap="round" stroke-linejoin="round"/></svg>
        <span>COMMERCIAL<br>WRAPS</span>
      </li>
    </ul>

    <div class="phone">
      <svg class="phone-icon" viewBox="0 0 24 24">
        <path d="M5 3l4 1 1 5-2.5 1.5a12 12 0 0 0 6 6L15 14l5 1 1 4-2 2C10 21 3 14 3 5z" fill="none" stroke="var(--brand-red)" stroke-width="2.2" stroke-linejoin="round"/>
        <path d="M14 3a7 7 0 0 1 7 7M14 7a3 3 0 0 1 3 3" fill="none" stroke="var(--brand-red)" stroke-width="2" stroke-linecap="round"/>
      </svg>
      <span>+1 604-555-0148</span>
    </div>
  </section>
</body>
</html>
```